"Quillfen" Paint Tools

Design logo and packaging for a range of paint tools. We need a bullseye style logo. Packaging background colour Pantone 425c. Main colours to be 2423c and 3015c. Attached is examples of another brand in our range for reference and for what we need the packaging to be on. Refer to attachments. We need designs in the di cuts for "50mm Wall Brush", "63mm Wall Brush, "75mm Wall Brush", "50mm Sash Cutter", "63mm Sash Cutter".

Requirements
Must have
• Quillfen Painting Tools

The Quillfen Brush range have been designed to give you the perfect finish for your painting project.

The brushes are made from the finest materials using the best craftsman.

The Quillfen Brushes use the latest filament technology to ensure that the brushes meet the performance demands of the professional painter. Our unique blend of high performance filament gives you the perfect balance between paint pick up, brush control, paint release and a smooth professional finish.

We provide a 100% quality guarantee

Made in China

```html
<!DOCTYPE html>
<html lang="en">
<head>
<meta charset="utf-8">
<title>Quillfen Paint Tools – Brush Packaging Die Cuts</title>
<link rel="stylesheet" href="https://fonts.googleapis.com/css2?family=Anton&family=Roboto:wght@400;500&family=Roboto+Condensed:wght@700&display=swap">
<style>
  :root {
    --charcoal: #55585a;
    --leaf-green: #7dc242;
    --sun-yellow: #fcc91e;
    --brand-green: #1fa23a;
    --label-white: #ffffff;
    --ink: #1d1d1b;
    --divider: #8a8a8a;
    --page: #ffffff;
  }
  html, body {
    margin: 0;
    padding: 0;
    width: 1200px;
    height: 2335px;
    overflow: hidden;
    background: var(--page);
  }
  .sheet { display: block; width: 1200px; height: 2335px; }
  .pack-charcoal { fill: var(--charcoal); }
  .pack-green { fill: var(--leaf-green); }
  .pack-yellow { fill: var(--sun-yellow); }
  .hang-hole, .label { fill: var(--label-white); }
  .brand-dot { fill: var(--brand-green); }
  .brand-name {
    font-family: "Roboto", sans-serif;
    font-weight: 500;
    fill: var(--ink);
    text-anchor: middle;
  }
  .product-name {
    font-family: "Anton", "Impact", sans-serif;
    fill: var(--ink);
  }
  .product-name.sash { font-size: 43px; }
  .product-name.wall { font-size: 47px; }
  .paint-types {
    font-family: "Roboto Condensed", "Arial Narrow", sans-serif;
    font-weight: 700;
    font-size: 10.5px;
    letter-spacing: 1.2px;
    fill: var(--ink);
  }
  .benefits {
    font-family: "Roboto", Arial, sans-serif;
    font-size: 10.2px;
    fill: var(--ink);
  }
  .size {
    font-family: "Anton", "Impact", sans-serif;
    font-size: 16px;
    fill: var(--ink);
    letter-spacing: 0.3px;
  }
  .size-divider { stroke: var(--divider); stroke-width: 0.8; }
</style>
</head>
<body>
<svg class="sheet" viewBox="0 0 780 1518" xmlns="http://www.w3.org/2000/svg">

  <!-- 63mm Sash Cutter – charcoal -->
  <g class="die-cut sash-charcoal">
    <path class="pack-charcoal" d="M97,210 L97,82 Q97,70 108,66 L200,47 L292,66 Q303,70 303,82 L303,208 L350,212 L310,620 L303,620 L303,632 L97,632 L97,620 L90,620 L52,212 Z"/>
    <rect class="hang-hole" x="170" y="175" width="60" height="36" rx="14"/>
    <rect class="label" x="110" y="220" width="180" height="388"/>
    <circle class="brand-dot" cx="200" cy="288" r="19"/>
    <text class="brand-name" x="200" y="350" font-size="30">Quillfen</text>
    <text class="product-name sash" x="136" y="437" textLength="130" lengthAdjust="spacingAndGlyphs">SASH</text>
    <text class="product-name sash" x="136" y="474" textLength="130" lengthAdjust="spacingAndGlyphs">CUTTER</text>
    <text class="paint-types" x="136" y="509">FOR ALL PAINT TYPES</text>
    <text class="benefits" x="136" y="527">Superior paint pick up, release,</text>
    <text class="benefits" x="136" y="542">control &amp; smooth finish</text>
    <text class="size" x="136" y="583">2.5 INCH</text>
    <line class="size-divider" x1="199" y1="569" x2="199" y2="583"/>
    <text class="size" x="205" y="583">63MM</text>
  </g>

  <!-- 63mm Wall Brush – charcoal -->
  <g class="die-cut wall-charcoal">
    <path class="pack-charcoal" d="M433,272 L433,118 Q433,106 445,102 L544,80 L643,102 Q655,106 655,118 L655,270 L722,276 L663,715 L655,715 L655,728 L433,728 L433,715 L425,715 L367,276 Z"/>
    <rect class="hang-hole" x="512" y="215" width="65" height="56" rx="16"/>
    <rect class="label" x="448" y="287" width="192" height="415"/>
    <circle class="brand-dot" cx="544" cy="355" r="22"/>
    <text class="brand-name" x="544" y="418" font-size="32">Quillfen</text>
    <text class="product-name wall" x="477" y="513" textLength="137" lengthAdjust="spacingAndGlyphs">WALL</text>
    <text class="product-name wall" x="477" y="560" textLength="137" lengthAdjust="spacingAndGlyphs">BRUSH</text>
    <text class="paint-types" x="477" y="595">FOR ALL PAINT TYPES</text>
    <text class="benefits" x="477" y="613">Superior paint pick up, release,</text>
    <text class="benefits" x="477" y="629">control &amp; smooth finish</text>
    <text class="size" x="477" y="672">2.5 INCH</text>
    <line class="size-divider" x1="540" y1="658" x2="540" y2="672"/>
    <text class="size" x="546" y="672">63MM</text>
  </g>

  <!-- 63mm Sash Cutter – green -->
  <g class="die-cut sash-green">
    <path class="pack-green" d="M128,807 L128,684 Q128,674 138,670 L230,648 L323,670 Q333,674 333,684 L333,805 L380,809 L340,1215 L333,1215 L333,1228 L128,1228 L128,1215 L122,1215 L82,809 Z"/>
    <rect class="hang-hole" x="200" y="770" width="62" height="36" rx="14"/>
    <rect class="label" x="142" y="820" width="178" height="390"/>
    <circle class="brand-dot" cx="231" cy="888" r="19"/>
    <text class="brand-name" x="231" y="950" font-size="30">Quillfen</text>
    <text class="product-name sash" x="166" y="1035" textLength="131" lengthAdjust="spacingAndGlyphs">SASH</text>
    <text class="product-name sash" x="166" y="1073" textLength="131" lengthAdjust="spacingAndGlyphs">CUTTER</text>
    <text class="paint-types" x="166" y="1107">FOR ALL PAINT TYPES</text>
    <text class="benefits" x="166" y="1125">Superior paint pick up, release,</text>
    <text class="benefits" x="166" y="1140">control &amp; smooth finish</text>
    <text class="size" x="166" y="1182">2.5 INCH</text>
    <line class="size-divider" x1="229" y1="1168" x2="229" y2="1182"/>
    <text class="size" x="235" y="1182">63MM</text>
  </g>

  <!-- 63mm Wall Brush – yellow -->
  <g class="die-cut wall-yellow">
    <path class="pack-yellow" d="M458,940 L458,786 Q458,774 470,770 L569,748 L668,770 Q680,774 680,786 L680,936 L748,942 L688,1380 L680,1380 L680,1393 L458,1393 L458,1380 L452,1380 L390,942 Z"/>
    <rect class="hang-hole" x="537" y="882" width="64" height="58" rx="16"/>
    <rect class="label" x="472" y="950" width="193" height="415"/>
    <circle class="brand-dot" cx="568" cy="1015" r="22"/>
    <text class="brand-name" x="568" y="1080" font-size="32">Quillfen</text>
    <text class="product-name wall" x="499" y="1175" textLength="139" lengthAdjust="spacingAndGlyphs">WALL</text>
    <text class="product-name wall" x="499" y="1222" textLength="139" lengthAdjust="spacingAndGlyphs">BRUSH</text>
    <text class="paint-types" x="499" y="1256">FOR ALL PAINT TYPES</text>
    <text class="benefits" x="499" y="1276">Superior paint pick up, release,</text>
    <text class="benefits" x="499" y="1291">control &amp; smooth finish</text>
    <text class="size" x="499" y="1335">2.5 INCH</text>
    <line class="size-divider" x1="562" y1="1321" x2="562" y2="1335"/>
    <text class="size" x="568" y="1335">63MM</text>
  </g>

</svg>
</body>
</html>
```